Business Card Design

Alder Ridge Living Homes, Inc. (ARLH, Inc.) is a private, non-profit corporation which provides an array of services to individuals in a community setting. These services include residential, vocational/day, and therapeutic recreation that afford individuals the opportunity to integrate into the community and participate as valued members of society. We work with individuals with developmental disabilities, traumatic brain injury and the elderly. We are a very small company with approximately 100 employees. We have been in business since 1975. We are looking for a business card that is professional, trendy and little out of the box. The Executive Director likes colors that are in the blue or green family. Open to add other colors to the design. The business card needs to include a house. We currently have a design on our old webpage that he likes. The webpage is alderridgelivinghomes.org. He likes that a lot. There is also a picture on our Facebook page that someone drew that he likes. This will be the business card for our entire agency. All administrative staff in our agency will have the same business card but have their information plugged in.

Industry/Entity Type

Non-Profit

Contact Information for Business Card

For questions you will need to contact me, Margaret Tolliver at 555-814-3067 ext. 208. The information below will be used for the business card:

Gerald Whitcombe, Executive Director
Alder Ridge Living Homes, Inc.
418 W. Elm Avenue - PO Box 356
Fernvale, EX 27819
gerald.whitcombe@arlhinc.example
555-814-3067 - work
555-862-4093 - cell
555-814-5518 - fax

Requirements
Must have
• I am really open when it comes to design. The only design that must be included is a house

```html
<!DOCTYPE html>
<html lang="en">
<head>
<meta charset="utf-8">
<title>Alder Ridge Living Homes – Business Card</title>
<link rel="stylesheet" href="https://fonts.googleapis.com/css2?family=Open+Sans:wdth,wght@75..100,600..800&display=swap">
<style>
  :root {
    --backdrop: #b2b2b2;
    --card: #ffffff;
    --ink-blue: #0f5474;
    --meadow: #879a65;
    --logo-tile: #f6d7a8;
    --logo-text: #ffffff;
  }
  * { margin: 0; padding: 0; box-sizing: border-box; }
  html, body {
    width: 1200px; height: 1000px; overflow: hidden;
    background: var(--backdrop);
  }
  .card {
    position: absolute; left: 238px; top: 281px;
    width: 737px; height: 419px;
    background: var(--card);
    overflow: hidden;
    font-family: "Open Sans", Arial, sans-serif;
    color: var(--ink-blue);
  }
  .card__wave { position: absolute; inset: 0; }
  .identity {
    position: absolute; left: 25px; top: 91px; width: 360px;
    text-align: center;
  }
  .identity__name {
    font-size: 28px; font-weight: 800; letter-spacing: 0.4px; line-height: 34px;
  }
  .identity__title {
    font-size: 21px; font-weight: 700; font-stretch: 75%; line-height: 26px;
    margin-top: 2px;
  }
  .contact {
    position: absolute; left: 380px; top: 68px;
    font-size: 20px; font-weight: 700; font-stretch: 75%; line-height: 26px;
  }
  .contact__lines { display: grid; grid-template-columns: 100px auto; row-gap: 6px; column-gap: 4px; }
  .contact__label { text-align: right; font-stretch: 100%; font-weight: 800; font-size: 18px; letter-spacing: 0.2px; }
  .contact__value { text-align: left; }
  .contact__email {
    position: absolute; right: 44px; top: 183px;
    font-size: 20px; font-weight: 700; font-stretch: 75%; line-height: 26px;
  }
  .contact__address {
    position: absolute; right: 44px; top: 231px;
    font-size: 20px; font-weight: 700; font-stretch: 75%;
    text-align: right; line-height: 24.5px;
  }
  .brand {
    position: absolute; left: 55px; top: 322px;
    display: flex; align-items: center; gap: 14px;
  }
  .brand__tile { width: 62px; height: 62px; background: var(--logo-tile); }
  .brand__name {
    color: var(--logo-text);
    font-size: 24px; font-weight: 700; font-stretch: 75%; line-height: 1.1;
  }
</style>
</head>
<body>
  <div class="card">
    <svg class="card__wave" width="737" height="419" viewBox="0 0 737 419" aria-hidden="true">
      <defs>
        <linearGradient id="sheen" x1="100" y1="0" x2="737" y2="0" gradientUnits="userSpaceOnUse">
          <stop offset="0" stop-color="#ffffff" stop-opacity="0"/>
          <stop offset="0.55" stop-color="#a9b595" stop-opacity="0.9"/>
          <stop offset="1" stop-color="#ffffff" stop-opacity="0.2"/>
        </linearGradient>
      </defs>
      <path d="M100,208 C220,215 330,240 430,272 C540,308 620,340 737,352 L737,353 C620,352 530,320 420,285 C300,247 160,222 100,222 Z" fill="url(#sheen)"/>
      <path d="M0,226 C150,220 300,245 420,285 C530,320 620,352 737,352 L737,419 L0,419 Z" fill="var(--meadow)"/>
    </svg>

    <div class="identity">
      <div class="identity__name">Gerald Whitcombe</div>
      <div class="identity__title">Executive director</div>
    </div>

    <div class="contact">
      <div class="contact__lines">
        <span class="contact__label">Phone:</span><span class="contact__value">555-814-3067</span>
        <span class="contact__label">Cell:</span><span class="contact__value">555-862-4093</span>
        <span class="contact__label">Fax:</span><span class="contact__value">555-814-5518</span>
      </div>
    </div>
    <div class="contact__email">gerald.whitcombe@arlhinc.example</div>
    <div class="contact__address">
      418 W. Elm Avenue<br>PO Box 356<br>Fernvale, EX<br>27819
    </div>

    <div class="brand">
      <div class="brand__tile"></div>
      <div class="brand__name">Alder Ridge Living<br>Homes, Inc.</div>
    </div>
  </div>
</body>
</html>
```